Company Introduction/Advertisement Flyer

We would like to redesign our current company line card. We send this printed flyer to prospective customers to introduce our company, the brands we represent and our competitive advantages. Our current design is very plain and simple, we'd like to have a little more design to the new version. Our website is www.valvequarryhub.com. We're a specialty supplier for plumbing material, specifically water and life safety products. Our customers are mostly male, blue-collar contractors, ages 40-60. I have included a pdf of our current flyer, and our high resolution transparent logo.

Requirements
Must have
• Phone number: (800) 314-2760
Website: www.valvequarryhub.com

```html
<!DOCTYPE html>
<html lang="en">
<head>
<meta charset="utf-8">
<title>Valve Quarry Supply Company – Line Card</title>
<link rel="stylesheet" href="https://fonts.googleapis.com/css2?family=Fira+Sans:wght@400;600;700&family=Noto+Serif:wght@400&display=swap">
<style>
  :root {
    --brand-red: #e30613;
    --brand-blue: #1a4fa0;
    --text-dark: #222222;
    --divider: #a8a8a8;
    --paper: #ffffff;
  }
  * { margin: 0; padding: 0; box-sizing: border-box; }
  html, body { width: 848px; height: 1200px; overflow: hidden; background: var(--paper); }
  .flyer { position: relative; width: 848px; height: 1200px; background: var(--paper); }

  .brand { position: absolute; left: 40px; top: 48px; display: flex; align-items: center; gap: 12px; }
  .brand-mark { width: 26px; height: 26px; background: var(--brand-red); }
  .brand-name { font-family: "Fira Sans", sans-serif; font-weight: 600; font-size: 27px; line-height: 1.05; color: var(--brand-blue); }
  .brand-name span { display: block; }

  .contact { position: absolute; left: 496px; top: 18px; }
  .contact-phone { font-family: "Fira Sans", sans-serif; font-weight: 700; font-size: 43px; color: var(--brand-red); letter-spacing: 0.5px; }
  .contact-line { font-family: "Noto Serif", serif; font-size: 19px; color: var(--brand-blue); line-height: 28px; }

  .hero-photo { position: absolute; left: 0; top: 156px; width: 848px; height: 533px;
    background: radial-gradient(ellipse at 30% 40%, #a89060 0%, #8d8a80 30%, #9a9894 60%, #878582 100%); }

  .offer { position: absolute; left: 40px; top: 722px; }
  .offer-title { font-family: "Fira Sans", sans-serif; font-weight: 700; font-size: 45px; line-height: 49px; color: var(--brand-red); }
  .offer-list { list-style: none; margin-top: 22px; font-family: "Noto Serif", serif; font-size: 20px; line-height: 28.2px; color: var(--brand-blue); }

  .divider { position: absolute; left: 379px; top: 717px; width: 3px; height: 424px; background: var(--divider); }

  .promise { position: absolute; left: 408px; top: 720px; width: 420px; }
  .promise-lead { font-family: "Fira Sans", sans-serif; font-weight: 700; font-size: 22.5px; line-height: 35.5px; color: var(--brand-blue); }
  .promise-list { list-style: none; margin-top: 20px; font-family: "Noto Serif", serif; font-size: 19.5px; line-height: 28.2px; color: var(--text-dark); }
  .promise-list li::before { content: "• "; }

  .brands { position: absolute; left: 20px; right: 20px; top: 1150px; height: 40px; display: flex; justify-content: space-between; align-items: center; }
  .brands span { font-family: "Fira Sans", sans-serif; font-weight: 700; font-size: 12px; color: var(--brand-blue); text-transform: uppercase; }
</style>
</head>
<body>
<div class="flyer">
  <header>
    <div class="brand">
      <div class="brand-mark"></div>
      <div class="brand-name"><span>Valve Quarry Supply</span><span>Company</span></div>
    </div>
    <div class="contact">
      <div class="contact-phone">(800) 314-2760</div>
      <div class="contact-line" style="margin-top:12px">24 hour Fax: (850) 314-2791</div>
      <div class="contact-line">www.valvequarryhub.com</div>
    </div>
  </header>

  <div class="hero-photo" role="img" aria-label="Photo of a brass backflow preventer assembly on concrete with repair parts, check valves, springs, screws and an adjustable wrench laid beside it"></div>

  <section class="offer">
    <h2 class="offer-title">YOUR<br>COMPLETE<br>SOURCE FOR:</h2>
    <ul class="offer-list">
      <li>Backflow Preventer Repair Parts</li>
      <li>Complete Assembles</li>
      <li>Specialty Tools</li>
      <li>Accessories</li>
      <li>Enclosures &amp; Cages</li>
      <li>Shutoff Valves</li>
      <li>Control Valves</li>
      <li>Test Gauge Calibration</li>
    </ul>
  </section>

  <div class="divider"></div>

  <section class="promise">
    <p class="promise-lead">We have the best customer service in the industry. We pride ourselves in being knowledgeable, courteous, and caring.</p>
    <ul class="promise-list">
      <li>Save gas and time by receiving parts at your doorstep</li>
      <li>1-2 day delivery anywhere in the country</li>
      <li>Same day shipping</li>
      <li>No minimum orders</li>
      <li>Online tracking of your order</li>
      <li>Friendly, knowledgable staff</li>
      <li>Technicians available to answer questions</li>
    </ul>
  </section>

  <footer class="brands">
    <span>Ridgeflo</span>
    <span>Tellmark Valves</span>
    <span>Arrowcrest</span>
    <span>Plainfield Instrument</span>
    <span>Kestrel</span>
    <span>Harbor Flow</span>
    <span>Linwood</span>
    <span>WarmVault</span>
    <span>Osprey Controls</span>
  </footer>
</div>
</body>
</html>
```